Create a 2-sided postcard design (standard size) for Torvane Systems, a professional low-voltage and security integration company.
Side 1 – Front (Marketing Side)
Headline / Intro:
"Torvane Systems – Security, Connectivity, and Peace of Mind."
Brief Overview / Summary:
Torvane Systems provides complete security and technology integration solutions for commercial, industrial, and multifamily properties. From access control to fire systems, we specialize in delivering seamless, scalable, and reliable installations supported by professional service and ongoing care.
Services Breakdown:
Access Control – Cloud-based and enterprise access solutions to manage entry and permissions.
CCTV / Video Surveillance – Protect your property with high-definition cameras and remote monitoring.
Intrusion Alarm – Professional-grade systems to detect and deter unauthorized access.
Audio-Visual – From conference rooms to distributed audio and digital displays.
Fire Systems – Code-compliant alarm systems with 24/7 UL monitoring and life-safety support.
Structured Data Cabling – Low-voltage and fiber cabling for reliable network infrastructure.
Trusted By (Logos):
Melo, Plivantex, Grovelink, Carrow Investments, Bluff Hardware, Pinefold Games, Ledgerline Property Consultants, TRUEform
Technology partners:
Include logos of brands like Quelt, Otter Bank Networks, RMT , Lumen Sentrywell, Solmira, JFT, Blazecor
Contact Info:
📧 sales@torvanesystems.example
📞 760-555-0142
🌐 torvanesystems.example
🖼️ Side 2 – Back (Branding Side)
Primary Focus:
Large, centered Torvane Systems logo.
Subtext / Tagline (Optional):
“Your Security and Technology Partner.”
List of Services (Under Logo):
Access Control | CCTV | Intrusion Alarm | Audio-Visual | Fire | Data
🎨 Design Preferences:
Clean, modern, and professional layout.
Corporate tones (e.g., black and white, bold accents).
Use clean typography and icons for service areas.
Logo should be prominent on the back and represent the brand with strength and clarity.
Open to designer layout and creative interpretation as long as it stays on brand.

```html
<!DOCTYPE html>
<html lang="en">
<head>
<meta charset="utf-8">
<title>Torvane Systems Postcard</title>
<link rel="stylesheet" href="https://fonts.googleapis.com/css2?family=Anton&family=Jost:wght@400;500;600&display=swap">
<style>
:root{
  --page:#8c8c8c;
  --ink:#0c121a;
  --ink-deep:#080c12;
  --violet:#6a5ff0;
  --violet-line:#5a50c8;
  --white:#ffffff;
  --soft:#d9dbe3;
  --icon:#b8bcc8;
  --bar-dark:#141416;
  --logo-ink:#2d2d3a;
}
*{box-sizing:border-box;margin:0;padding:0}
html,body{width:1200px;height:2396px;overflow:hidden;background:var(--page)}
body{position:relative;font-family:"Jost",sans-serif;color:var(--white)}
.card{position:absolute;left:60px;width:1080px;height:720px;overflow:hidden;background:var(--ink)}
.card--front{top:420px}
.card--back{top:1260px}

/* brand lockup */
.brand{position:absolute;display:flex;align-items:center;gap:16px;font-family:"Jost",sans-serif;font-weight:500;color:var(--white)}
.brand__square{border:4px solid var(--white)}
.brand__words{display:flex;flex-direction:column;line-height:1}
.brand__name{letter-spacing:1px}
.brand__sub{letter-spacing:.34em}

.card--front .brand{left:50px;top:42px}
.card--front .brand__square{width:58px;height:58px}
.card--front .brand__name{font-size:54px}
.card--front .brand__sub{font-size:29px;margin-top:4px}

.headline-rule{position:absolute;left:392px;top:32px;width:2px;height:110px;background:var(--soft)}
.headline{position:absolute;left:432px;top:22px;font-family:"Anton",sans-serif;font-size:58px;line-height:66px;color:var(--violet);letter-spacing:.5px}

.intro{position:absolute;left:60px;right:60px;top:164px;text-align:center;font-size:15.5px;line-height:20px;color:var(--white)}

/* services frame */
.services-frame{position:absolute;left:38px;right:38px;top:248px;height:240px;border:1.5px solid var(--violet-line);border-bottom:none;border-radius:18px 18px 0 0}
.pill{position:absolute;left:50%;transform:translateX(-50%);background:var(--violet);color:var(--white);font-weight:500;letter-spacing:.5px;text-align:center;border-radius:0 0 12px 12px;white-space:nowrap}
.card--front .pill{top:-2px;font-size:23px;padding:2px 22px 4px}

.service-list{position:absolute;top:302px;left:78px;width:940px;display:grid;grid-template-columns:470px 470px;row-gap:12px}
.service{display:flex;gap:14px;font-size:15.5px;line-height:20px;color:var(--white)}
.service__icon{flex:0 0 32px;height:32px;margin-top:2px}
.service__name{color:var(--violet)}

.signal-band{position:absolute;left:0;right:0;height:78px;background:linear-gradient(180deg,rgba(12,18,26,0) 0%,rgba(120,128,150,.22) 55%,rgba(160,168,190,.30) 100%)}
.card--front .signal-band{top:440px}
.card--back .signal-band{top:562px}

/* logo strip */
.logo-strip{position:absolute;left:0;right:0;top:518px;height:112px;background:var(--white);color:var(--logo-ink)}
.strip-label{position:absolute;top:56px;transform:translate(-50%,-50%) rotate(-90deg);font-size:13px;font-weight:600;line-height:14px;color:var(--violet);text-align:center;white-space:nowrap}
.strip-label--trusted{left:52px}
.strip-label--partners{left:576px}
.strip-rule{position:absolute;left:534px;top:16px;width:1.5px;height:82px;background:var(--logo-ink)}
.logo-grid{position:absolute;top:12px;height:88px;display:grid;grid-template-columns:repeat(4,1fr);align-items:center;justify-items:center;column-gap:10px}
.logo-grid--trusted{left:88px;width:430px}
.logo-grid--partners{left:604px;width:456px}
.partner-name{font-family:"Jost",sans-serif;font-weight:500;font-size:17px;line-height:17px;text-align:center;color:var(--logo-ink)}
.partner-name--small{font-size:12.5px;line-height:13px}

/* contact bar */
.contact-bar{position:absolute;left:0;right:0;top:650px;height:70px}
.contact-bar__dark{position:absolute;left:400px;right:0;top:10px;bottom:12px;background:var(--bar-dark)}
.contact-bar__phone{position:absolute;left:0;top:0;width:420px;height:100%;background:var(--violet);clip-path:polygon(0 0,94% 0,100% 100%,0 100%);display:flex;align-items:center;padding-left:42px;gap:6px;font-size:44px;font-weight:500;letter-spacing:.5px;color:var(--white)}
.contact-bar__web{position:absolute;left:460px;right:40px;top:10px;bottom:12px;display:flex;align-items:center;gap:10px;font-size:24px;color:var(--white);white-space:nowrap}
.contact-bar__web .sep{margin:0 4px}

/* back */
.back-photo{position:absolute;inset:0;background:radial-gradient(ellipse at 50% 40%,#1f2a3c 0%,#141c2a 50%,#0b1119 100%)}
.card--back .brand{left:50%;transform:translateX(-50%);top:46px;gap:24px}
.card--back .brand__square{width:110px;height:110px;border-width:6px}
.card--back .brand__name{font-size:104px}
.card--back .brand__sub{font-size:54px;margin-top:6px}
.tagline{position:absolute;left:0;right:0;top:228px;text-align:center;font-family:"Anton",sans-serif;font-size:54px;line-height:64px;color:var(--violet);letter-spacing:.5px}
.card--back .services-frame{top:320px;height:270px}
.card--back .pill{top:-2px;font-size:25px;padding:2px 28px 4px}
.service-row{position:absolute;left:60px;right:60px;top:392px;display:flex;justify-content:space-between}
.service-tile{display:flex;flex-direction:column;align-items:center;width:150px}
.service-tile__circle{width:88px;height:88px;border-radius:50%;background:var(--white);display:flex;align-items:center;justify-content:center}
.service-tile__label{margin-top:26px;font-size:27px;color:var(--violet);white-space:nowrap}
</style>
</head>
<body>

<!-- FRONT -->
<section class="card card--front">
  <div class="brand">
    <span class="brand__square"></span>
    <div class="brand__words"><span class="brand__name">TORVANE</span><span class="brand__sub">SYSTEMS</span></div>
  </div>
  <div class="headline-rule"></div>
  <h1 class="headline">SECURITY, CONNECTIVITY,<br>AND PEACE OF MIND.</h1>
  <p class="intro">Torvane Systems provides complete security and technology integration solutions for commercial, industrial, and multifamily properties. From access control to fire systems, we specialize in delivering seamless, scalable, and reliable installations supported by professional service and ongoing care.</p>

  <div class="services-frame"><div class="pill">SERVICES BREAKDOWN</div></div>

  <div class="service-list">
    <div class="service">
      <svg class="service__icon" viewBox="0 0 32 32" fill="none" stroke="var(--icon)" stroke-width="1.6"><path d="M10 14v-4a6 6 0 0 1 12 0v4"/><rect x="7" y="14" width="18" height="15" rx="1"/><path d="M16 20v4"/></svg>
      <p><span class="service__name">Access Control –</span> Cloud-based and enterprise access solutions to manage entry and permissions.</p>
    </div>
    <div class="service">
      <svg class="service__icon" viewBox="0 0 32 32" fill="none" stroke="var(--icon)" stroke-width="1.6"><rect x="4" y="5" width="24" height="16" rx="1"/><path d="M10 9h12M10 13h8M16 21v5M10 27h12"/></svg>
      <p><span class="service__name">Audio-Visual –</span> From conference rooms to distributed audio and digital displays.</p>
    </div>
    <div class="service">
      <svg class="service__icon" viewBox="0 0 32 32" fill="none" stroke="var(--icon)" stroke-width="1.6"><circle cx="16" cy="16" r="13"/><circle cx="16" cy="16" r="7"/></svg>
      <p><span class="service__name">CCTV / Video Surveillance –</span> Protect your property with high-definition cameras and remote monitoring.</p>
    </div>
    <div class="service">
      <svg class="service__icon" viewBox="0 0 32 32" fill="var(--icon)"><path d="M16 3c2 5 9 9 9 17a9 9 0 0 1-18 0c0-5 3-7 4-10 1 3 2 4 3 4 0-4 0-7 2-11z"/></svg>
      <p><span class="service__name">Fire Systems –</span> Code-compliant alarm systems with 24/7 UL monitoring and life-safety support.</p>
    </div>
    <div class="service">
      <svg class="service__icon" viewBox="0 0 32 32" fill="none" stroke="var(--icon)" stroke-width="1.5"><circle cx="6" cy="6" r="3"/><circle cx="16" cy="6" r="3"/><circle cx="26" cy="6" r="3"/><circle cx="6" cy="16" r="3"/><circle cx="16" cy="16" r="3"/><circle cx="26" cy="16" r="3"/><circle cx="6" cy="26" r="3"/><circle cx="16" cy="26" r="3"/><circle cx="26" cy="26" r="3"/></svg>
      <p><span class="service__name">Intrusion Alarm –</span> Professional-grade systems to detect and deter unauthorized access.</p>
    </div>
    <div class="service">
      <svg class="service__icon" viewBox="0 0 32 32" fill="none" stroke="var(--icon)" stroke-width="1.6"><rect x="9" y="3" width="19" height="24" rx="1"/><path d="M13 9h11M13 13h11M13 17h11M13 21h7"/><path d="M4 14v13h5M4 20h5"/></svg>
      <p><span class="service__name">Structured Data Cabling –</span> Low-voltage and fiber cabling for reliable network infrastructure.</p>
    </div>
  </div>

  <div class="signal-band" role="img" aria-label="Soft band of fine vertical signal lines"></div>

  <div class="logo-strip">
    <span class="strip-label strip-label--trusted">TRUSTED<br>BY</span>
    <div class="logo-grid logo-grid--trusted">
      <span class="partner-name">Melo</span>
      <span class="partner-name">Plivantex</span>
      <span class="partner-name">Grovelink</span>
      <span class="partner-name">TRUEform</span>
      <span class="partner-name partner-name--small">Pinefold Games</span>
      <span class="partner-name">Bluff Hardware</span>
      <span class="partner-name partner-name--small">Carrow Investments</span>
      <span class="partner-name partner-name--small">Ledgerline Property Consultants</span>
    </div>
    <div class="strip-rule"></div>
    <span class="strip-label strip-label--partners">TECHNOLOGY<br>PARTNERS</span>
    <div class="logo-grid logo-grid--partners">
      <span class="partner-name">Quelt</span>
      <span class="partner-name partner-name--small">Otter Bank Networks</span>
      <span class="partner-name">Solmira</span>
      <span></span>
      <span class="partner-name partner-name--small">Lumen Sentrywell</span>
      <span class="partner-name">RMT</span>
      <span class="partner-name">JFT</span>
      <span class="partner-name">Blazecor</span>
    </div>
  </div>

  <div class="contact-bar">
    <div class="contact-bar__dark"></div>
    <div class="contact-bar__phone">
      <svg width="30" height="36" viewBox="0 0 24 28" fill="var(--white)"><path d="M7 1l4 6-3 3c1 4 3 7 6 9l3-2 5 5-3 4C9 25 2 14 3 4z"/></svg>
      760-555-0142
    </div>
    <div class="contact-bar__web">
      <svg width="18" height="14" viewBox="0 0 18 14" fill="none" stroke="var(--soft)" stroke-width="1.4"><rect x="1" y="1" width="16" height="12"/><path d="M1 1l8 7 8-7"/></svg>
      sales@torvanesystems.example <span class="sep">|</span>
      <svg width="16" height="16" viewBox="0 0 16 16" fill="none" stroke="var(--violet)" stroke-width="1.4"><circle cx="8" cy="8" r="7"/><path d="M1 8h14M8 1c3 3 3 11 0 14M8 1c-3 3-3 11 0 14"/></svg>
      torvanesystems.example
    </div>
  </div>
</section>

<!-- BACK -->
<section class="card card--back">
  <div class="back-photo" role="img" aria-label="Dim, blue-toned photo of a modern office interior"></div>

  <div class="brand">
    <span class="brand__square"></span>
    <div class="brand__words"><span class="brand__name">TORVANE</span><span class="brand__sub">SYSTEMS</span></div>
  </div>
  <h2 class="tagline">YOUR SECURITY AND TECHNOLOGY PARTNER</h2>

  <div class="services-frame"><div class="pill">OUR SERVICES</div></div>

  <div class="service-row">
    <div class="service-tile">
      <div class="service-tile__circle"><svg width="44" height="44" viewBox="0 0 32 32" fill="none" stroke="#444" stroke-width="1.4"><path d="M10 14v-4a6 6 0 0 1 12 0v4"/><rect x="7" y="14" width="18" height="15" rx="1"/><path d="M16 20v4"/></svg></div>
      <span class="service-tile__label">Access Control</span>
    </div>
    <div class="service-tile">
      <div class="service-tile__circle"><svg width="48" height="48" viewBox="0 0 32 32" fill="none" stroke="#444" stroke-width="1.3"><circle cx="16" cy="16" r="13"/><circle cx="16" cy="16" r="8"/></svg></div>
      <span class="service-tile__label">CCTV</span>
    </div>
    <div class="service-tile">
      <div class="service-tile__circle"><svg width="44" height="44" viewBox="0 0 32 32" fill="none" stroke="#444" stroke-width="1.3"><circle cx="6" cy="6" r="3"/><circle cx="16" cy="6" r="3"/><circle cx="26" cy="6" r="3"/><circle cx="6" cy="16" r="3"/><circle cx="16" cy="16" r="3"/><circle cx="26" cy="16" r="3"/><circle cx="6" cy="26" r="3"/><circle cx="16" cy="26" r="3"/><circle cx="26" cy="26" r="3"/></svg></div>
      <span class="service-tile__label">Intrusion Alarm</span>
    </div>
    <div class="service-tile">
      <div class="service-tile__circle"><svg width="44" height="44" viewBox="0 0 32 32" fill="#333"><path d="M16 3c2 5 9 9 9 17a9 9 0 0 1-18 0c0-5 3-7 4-10 1 3 2 4 3 4 0-4 0-7 2-11z"/></svg></div>
      <span class="service-tile__label">Fire</span>
    </div>
    <div class="service-tile">
      <div class="service-tile__circle"><svg width="48" height="48" viewBox="0 0 32 32" fill="none" stroke="#444" stroke-width="1.4"><rect x="4" y="5" width="24" height="16" rx="1"/><path d="M10 9h12M10 13h8M16 21v5M10 27h12"/></svg></div>
      <span class="service-tile__label">Audio-Visual</span>
    </div>
    <div class="service-tile">
      <div class="service-tile__circle"><svg width="46" height="46" viewBox="0 0 32 32" fill="none" stroke="#444" stroke-width="1.4"><rect x="9" y="3" width="19" height="24" rx="1"/><path d="M13 9h11M13 13h11M13 17h11M13 21h7"/><path d="M4 14v13h5M4 20h5"/></svg></div>
      <span class="service-tile__label">Data</span>
    </div>
  </div>

  <div class="signal-band" role="img" aria-label="Soft band of fine vertical signal lines"></div>

  <div class="contact-bar">
    <div class="contact-bar__dark"></div>
    <div class="contact-bar__phone">
      <svg width="30" height="36" viewBox="0 0 24 28" fill="var(--white)"><path d="M7 1l4 6-3 3c1 4 3 7 6 9l3-2 5 5-3 4C9 25 2 14 3 4z"/></svg>
      760-555-0142
    </div>
    <div class="contact-bar__web">
      <svg width="18" height="14" viewBox="0 0 18 14" fill="none" stroke="var(--soft)" stroke-width="1.4"><rect x="1" y="1" width="16" height="12"/><path d="M1 1l8 7 8-7"/></svg>
      sales@torvanesystems.example <span class="sep">|</span>
      <svg width="16" height="16" viewBox="0 0 16 16" fill="none" stroke="var(--violet)" stroke-width="1.4"><circle cx="8" cy="8" r="7"/><path d="M1 8h14M8 1c3 3 3 11 0 14M8 1c-3 3-3 11 0 14"/></svg>
      torvanesystems.example
    </div>
  </div>
</section>

</body>
</html>
```